Need help revamping our cards for Prescription Assistance Program

Would like to go with something in a Black Theme that grabs attention and looks official. I have included some of our previous designs. The Blue/White version is our most current version so would like to follow its format regarding the information. Perhaps, one side white, the other black(might be different/catchy)
Cards are not to have pharmacy logos. Would like to have the ability to update cards with new member IDs. Would also desire a continued relationship with the designer to update and/or modify for regional needs.
Thank you

needs information stacked on the right side for easy viewing whilst flipping through a stack of competitor's cards

please include VELMAR Code

Target Market(s)

pharmacies(pharmacist, techs), general public

Requirements
Must have
• eye catching, official looking, information aragned in an easy to view format, desired to standout if in an stack of 20 other cards
Should not have
• pharmacy logos

```html
<!DOCTYPE html>
<html lang="en">
<head>
<meta charset="utf-8">
<title>ScriptPlus Discount Prescription Drug Card</title>
<link href="https://fonts.googleapis.com/css2?family=Lato:wght@400;700;900&display=swap" rel="stylesheet">
<style>
  :root {
    --ink: #0b0b0c;
    --red: #ff2222;
    --paper: #ffffff;
    --stage: #2b2630;
  }
  * { box-sizing: border-box; margin: 0; padding: 0; }
  html, body { width: 1200px; height: 800px; overflow: hidden; }
  body {
    background: var(--stage);
    font-family: "Lato", sans-serif;
    position: relative;
  }
  .card {
    position: absolute;
    top: 252px;
    width: 520px;
    height: 297px;
    overflow: hidden;
    background: var(--ink);
    box-shadow: 0 18px 40px rgba(0,0,0,.45);
  }
  .card--front { left: 50px; }
  .card--back { left: 630px; }
  .card__shapes { position: absolute; inset: 0; width: 100%; height: 100%; }

  .brand { position: absolute; color: var(--paper); }
  .brand__name {
    display: flex; align-items: center; gap: 8px;
    font-weight: 900; font-size: 40px; letter-spacing: -1px; line-height: 1;
  }
  .brand__dot { width: 12px; height: 12px; background: var(--red); flex: none; }
  .brand__tagline {
    margin-top: 6px; font-weight: 700; font-size: 8.5px;
    letter-spacing: 1.6px; text-transform: uppercase;
  }
  .card--front .brand { left: 205px; top: 104px; }
  .card--back .brand { left: 300px; top: 112px; }
  .card--back .brand__name { font-size: 34px; }
  .card--back .brand__tagline { font-size: 7px; }

  .website {
    position: absolute; left: 106px; top: 210px;
    font-weight: 900; font-size: 19px; color: var(--ink);
    transform: rotate(4deg);
    transform-origin: left center;
  }

  .benefits {
    position: absolute; left: 34px; top: 58px;
    list-style: none; color: var(--paper); font-size: 13px; line-height: 1.3;
  }
  .benefits li { display: flex; align-items: center; gap: 8px; }
  .benefits li::before {
    content: ""; width: 6px; height: 6px; border-radius: 50%;
    background: var(--red); flex: none;
  }
  .helpline {
    position: absolute; left: 34px; top: 150px; width: 250px;
    color: var(--paper); font-size: 11.5px; line-height: 1.35;
  }
  .member {
    position: absolute; left: 394px; top: 224px;
    color: var(--paper); font-size: 21px; line-height: 1.15; letter-spacing: 1px;
  }
</style>
</head>
<body>

<section class="card card--front" aria-label="Card front">
  <svg class="card__shapes" viewBox="0 0 520 297" aria-hidden="true">
    <path d="M0 0 H520 V10 C420 14 380 40 300 50 C200 64 100 70 0 80 Z" fill="var(--red)"/>
    <path d="M320 56 C400 42 460 32 520 30 V42 C450 46 400 58 335 64 Z" fill="var(--paper)"/>
    <path d="M0 92 C50 92 66 120 70 160 C76 230 170 264 300 266 C380 266 430 236 520 238 V297 H0 Z" fill="var(--red)"/>
    <path d="M80 172 C86 210 110 238 180 248 H316 Q338 248 330 228 C322 208 290 200 220 194 C160 188 110 184 80 172 Z" fill="var(--paper)"/>
  </svg>
  <div class="brand">
    <div class="brand__name"><span class="brand__dot"></span>ScriptPlus</div>
    <div class="brand__tagline">Discount Prescription Drug Card</div>
  </div>
  <div class="website">www.ScriptPlus.com</div>
</section>

<section class="card card--back" aria-label="Card back">
  <svg class="card__shapes" viewBox="0 0 520 297" aria-hidden="true">
    <path d="M0 0 H520 V28 C470 28 440 42 400 44 H0 Z" fill="var(--red)"/>
    <path d="M300 100 C360 84 430 78 520 80 V100 C440 98 380 102 300 100 Z" fill="var(--paper)"/>
    <path d="M0 188 C100 184 180 188 215 203 C170 197 90 197 0 199 Z" fill="var(--red)"/>
    <path d="M0 206 C120 200 200 206 235 230 C255 245 250 265 230 274 H0 Z" fill="var(--paper)"/>
    <path d="M0 290 H220 C260 290 270 240 320 218 C380 200 460 210 520 212 V297 H0 Z" fill="var(--red)"/>
  </svg>
  <ul class="benefits">
    <li>100% HIPAA Compliant</li>
    <li>up to 90% instant savings</li>
    <li>Always savings to LOWER of PRICING</li>
    <li>Largest savings on FAST MOVERS</li>
  </ul>
  <p class="helpline">If you are unable to process a prescription through the programme, call (866) 555-0142</p>
  <div class="brand">
    <div class="brand__name"><span class="brand__dot"></span>ScriptPlus</div>
    <div class="brand__tagline">Discount Prescription Drug Card</div>
  </div>
  <div class="member">VELMAR<br>40917</div>
</section>

</body>
</html>
```